Health & Nutrition - Business Cards

Needs to look new-age, simple, and elegant. The cards are for my services/counsel in health and nutrition - which include mind, body, and soul. I would like to see something clean and simple but beautiful. Can have a plain background or with a pattern but I don't want it to take away from my contact details. Therefore, my info can be on the back of the card and a nice front design. I really like the flower of life symbol. The name of my business is called Velvet Meadow.

Target Market(s)

Clients - men & women age 20-60. Adults, parents, teachers, sick individuals seeking nutrient counseling and dietary management.

Industry/Entity Type

Nutritionist

Contact Information for Business Card

Tomas Brindle
Cell: 345-827-4602
Email: tbrindle@quillpost.example

Colors
33a6d7
33b8a4
add136
ffffff
5c5c5c
f04a50
fbee3f
cedeed
85cae6

Requirements
Nice to have
• Maybe it can have some sort of sacred geometry as well, but not required. Nice to have the colors that I choose in the project but feel free to come up with your own use of colors. Thanks! =)

```html
<!DOCTYPE html>
<html lang="en">
<head>
<meta charset="utf-8">
<title>Velvet Meadow – Business Cards</title>
<link href="https://fonts.googleapis.com/css2?family=Marcellus&family=Open+Sans:wght@400&display=swap" rel="stylesheet">
<style>
  :root {
    --backdrop: #d9dadb;
    --card-dark: #1e1e1e;
    --card-light: #f4f4f2;
    --ink-light: #f2f2f2;
    --ink-grey: #5c5c5c;
    --leaf: #7cbf4a;
    --shadow: rgba(0,0,0,0.18);
  }
  html, body {
    margin: 0;
    width: 1200px;
    height: 1200px;
    overflow: hidden;
    background: var(--backdrop);
  }
  .canvas {
    width: 1200px;
    height: 1200px;
    display: flex;
    flex-direction: column;
    align-items: center;
    justify-content: center;
    gap: 80px;
  }
  .card {
    position: relative;
    width: 700px;
    height: 400px;
    box-shadow: 0 6px 18px var(--shadow);
    box-sizing: border-box;
    overflow: hidden;
  }
  .card--front { background: var(--card-dark); }
  .card--back { background: var(--card-light); }

  .brand {
    font-family: "Marcellus", "Optima", serif;
    font-weight: 400;
    margin: 0;
    white-space: nowrap;
    line-height: 1.2;
  }
  .brand__dot {
    display: inline-block;
    border-radius: 50%;
    background: var(--leaf);
  }

  .card--front .brand {
    position: absolute;
    left: 50%;
    top: 50%;
    transform: translate(-50%, -50%);
    display: flex;
    align-items: center;
    gap: 18px;
    font-size: 56px;
    color: var(--ink-light);
  }
  .card--front .brand__dot {
    width: 22px;
    height: 22px;
    flex: none;
  }

  .card--back .brand {
    position: absolute;
    left: 300px;
    top: 128px;
    font-size: 40px;
    color: var(--ink-grey);
  }
  .card--back .brand__dot {
    position: absolute;
    left: -180px;
    top: -58px;
    width: 44px;
    height: 44px;
  }
  .holder {
    position: absolute;
    left: 64px;
    top: 150px;
    margin: 0;
    font-family: "Marcellus", "Optima", serif;
    font-size: 32px;
    font-weight: 400;
    line-height: 1.2;
    white-space: nowrap;
    color: var(--ink-grey);
  }
  .contact {
    position: absolute;
    left: 320px;
    top: 212px;
    margin: 0;
    padding: 0;
    list-style: none;
    font-family: "Open Sans", Arial, sans-serif;
    font-size: 18px;
    line-height: 1.6;
    white-space: nowrap;
    color: var(--ink-grey);
  }
  .contact__label { display: inline-block; min-width: 54px; }
</style>
</head>
<body>
  <main class="canvas">
    <section class="card card--front" aria-label="Card front">
      <h1 class="brand"><span class="brand__dot" aria-hidden="true"></span>Velvet Meadow</h1>
    </section>

    <section class="card card--back" aria-label="Card back">
      <h2 class="brand"><span class="brand__dot" aria-hidden="true"></span>Velvet Meadow</h2>
      <p class="holder">Tomas Brindle</p>
      <ul class="contact">
        <li><span class="contact__label">Cell</span>: 345-827-4602</li>
        <li>Email: tbrindle@quillpost.example</li>
      </ul>
    </section>
  </main>
</body>
</html>
```